Harbor Compass - Book Cover

I need a book cover for my debut work, "Harbor Compass - Turning the Tide, One Step at a Time." While the website isn't complete, you can get a sense of what I am writing about by looking at my website, harborcompassbooks.org. The book is a leadership development book, but more of a personal change journey. The emphasis is on figuring out how to combine you work, social, and own self into an authentic package that not only resonates with others, but makes what you achieve more fulfilling.

I am attaching a copy of my logo so you can get a sense of what I like. I would prefer to not have the cover be photographic, but am open to suggestions. This will be a series of books so maintaining some sense of style will be important, and can garner future work.

Industry/Entity Type

Leadership

```html
<!DOCTYPE html>
<html lang="en">
<head>
<meta charset="utf-8">
<title>Harbor Compass – Book Cover</title>
<link rel="stylesheet" href="https://fonts.googleapis.com/css2?family=Roboto+Slab:wght@700;800&family=Courier+Prime:wght@700&display=swap">
<style>
  :root {
    --page-bg: #ffffff;
    --spine-blue-light: #2ea3f2;
    --spine-blue-dark: #0c6fc4;
    --title-blue: #0a5fb0;
    --brand-white: #ffffff;
    --sky-top: #3c3d3c;
    --sky-upper: #7a7a72;
    --glow-core: #fffdf5;
    --glow-warm: #f5ead0;
    --arm-tan: #c29a62;
    --arm-shadow: #8f6e45;
    --cloud-blue: #6f818d;
    --cloud-light: #dde3e6;
  }
  * { margin: 0; padding: 0; box-sizing: border-box; }
  html, body {
    width: 1200px;
    height: 1000px;
    overflow: hidden;
    background: var(--page-bg);
  }
  .canvas {
    position: relative;
    width: 1200px;
    height: 1000px;
  }
  .book {
    position: absolute;
    left: 300px;
    top: 75px;
    display: flex;
    height: 850px;
    box-shadow: 0 14px 40px rgba(0, 0, 0, 0.18);
  }
  .spine {
    position: relative;
    width: 52px;
    height: 100%;
    background: linear-gradient(90deg, var(--spine-blue-light), var(--spine-blue-dark));
  }
  .spine-title,
  .spine-author {
    position: absolute;
    left: 50%;
    white-space: nowrap;
    color: var(--brand-white);
    transform-origin: left center;
    transform: rotate(90deg) translateY(-50%);
  }
  .spine-title {
    top: 24px;
    font-family: "Roboto Slab", Rockwell, Georgia, serif;
    font-weight: 800;
    font-size: 19px;
    letter-spacing: 0.5px;
  }
  .spine-author {
    top: 690px;
    font-family: "Courier Prime", "Courier New", monospace;
    font-weight: 700;
    font-size: 17px;
  }
  .front-cover {
    position: relative;
    width: 548px;
    height: 100%;
    overflow: hidden;
  }
  .cover-photo {
    position: absolute;
    inset: 0;
    background:
      radial-gradient(ellipse 42% 20% at 32% 42%, var(--glow-core) 0%, rgba(255, 253, 245, 0.85) 45%, rgba(255, 253, 245, 0) 100%),
      radial-gradient(ellipse 40% 22% at 60% 30%, var(--glow-warm) 0%, rgba(245, 234, 208, 0) 100%),
      linear-gradient(100deg, rgba(194, 154, 98, 0) 48%, var(--arm-tan) 56%, var(--arm-shadow) 68%, rgba(143, 110, 69, 0) 76%),
      radial-gradient(ellipse 40% 30% at 95% 62%, var(--cloud-blue) 0%, rgba(111, 129, 141, 0) 100%),
      linear-gradient(180deg, var(--sky-top) 0%, var(--sky-upper) 22%, #c9c8bd 42%, var(--cloud-light) 75%, #b9c4ca 100%);
  }
  .brand {
    position: absolute;
    top: 56px;
    left: 22px;
    display: flex;
    align-items: center;
    gap: 12px;
  }
  .brand-mark {
    width: 40px;
    height: 40px;
    border-radius: 50%;
    background: var(--spine-blue-dark);
  }
  .brand-name {
    font-family: "Roboto Slab", Rockwell, Georgia, serif;
    font-weight: 800;
    font-size: 26px;
    color: var(--brand-white);
    letter-spacing: 0.5px;
  }
  .cover-title {
    position: absolute;
    top: 268px;
    left: 28px;
    width: 220px;
    text-align: right;
    font-family: "Roboto Slab", Rockwell, Georgia, serif;
    font-weight: 800;
    font-size: 29px;
    line-height: 1.12;
    color: var(--title-blue);
  }
</style>
</head>
<body>
  <main class="canvas">
    <article class="book">
      <aside class="spine">
        <span class="spine-title">HARBOR COMPASS</span>
        <span class="spine-author">by writer name</span>
      </aside>
      <section class="front-cover">
        <div class="cover-photo" role="img" aria-label="Photo of a raised dusty fist holding a gold first-place medal on a ribbon against a bright cloudy sky"></div>
        <header class="brand">
          <span class="brand-mark"></span>
          <span class="brand-name">HARBOR COMPASS</span>
        </header>
        <h1 class="cover-title">Turning<br>the Tide,<br>One Step<br>at a Time</h1>
      </section>
    </article>
  </main>
</body>
</html>
```